Business Card Design for a Software Startup

We'd like to have a business card design. We already have a logo. Basically what we need is a clean design with name, address, cellphone and phone numbers, e-mail and web site address (front) and a space on the back with our logo with the company name on the right side and some texts on the bottom.
We are a development and consulting company in Brazil with highly qualified team of professionals in Java, iOS and Android development and consulting.

Target Market(s)

CIO, IT managers of mid to big size companies

Industry/Entity Type

Business

```html
<!DOCTYPE html>
<html lang="en">
<head>
<meta charset="utf-8">
<title>Trelvix – Business Card</title>
<link rel="stylesheet" href="https://fonts.googleapis.com/css2?family=Source+Sans+3:wght@400;600;700&display=swap">
<style>
  :root {
    --ink: #1f3f78;
    --ink-soft: #2a4a80;
    --frame: #9fd3ee;
    --band-start: #00aeef;
    --band-mid: #1583c0;
    --band-end: #3d3d6b;
    --mark: #1a6fae;
    --paper: #ffffff;
  }
  * { margin: 0; padding: 0; box-sizing: border-box; }
  html, body {
    width: 1200px;
    height: 849px;
    overflow: hidden;
    background: var(--paper);
    font-family: "Source Sans 3", sans-serif;
    color: var(--ink);
  }
  .canvas { position: relative; width: 1200px; height: 849px; }
  .card {
    position: absolute;
    left: 141px;
    top: 151px;
    width: 924px;
    height: 502px;
    border: 1px solid var(--frame);
    background: var(--paper);
  }
  .band {
    position: absolute;
    left: 454px;
    width: 470px;
    height: 31px;
    background: linear-gradient(90deg, var(--band-start) 0%, var(--band-mid) 45%, var(--band-end) 100%);
  }
  .band--top { top: -1px; }
  .band--bottom { bottom: -1px; }

  .brand {
    position: absolute;
    left: 0;
    width: 454px;
    top: 114px;
    display: flex;
    flex-direction: column;
    align-items: center;
  }
  .brand__square {
    width: 214px;
    height: 214px;
    border-radius: 26px;
    background: var(--mark);
  }
  .brand__name {
    margin-top: 14px;
    font-size: 52px;
    font-weight: 700;
    letter-spacing: 1px;
    line-height: 1;
    color: var(--ink);
  }
  .brand__web {
    position: absolute;
    left: 0;
    width: 454px;
    top: 456px;
    text-align: center;
    font-size: 19px;
    line-height: 24px;
    color: var(--ink-soft);
  }

  .details {
    position: absolute;
    left: 523px;
    top: 70px;
  }
  .details__name {
    font-size: 36px;
    font-weight: 400;
    line-height: 1.2;
  }
  .details__role {
    margin-top: 30px;
    font-size: 25px;
    line-height: 1.2;
  }
  .details__address {
    margin-top: 60px;
    font-size: 22px;
    line-height: 33px;
    font-style: normal;
  }
  .details__contact {
    margin-top: 33px;
    font-size: 22px;
    line-height: 33px;
    list-style: none;
  }
  .details__label { display: inline-block; width: 46px; }
</style>
</head>
<body>
<main class="canvas">
  <section class="card" aria-label="Business card">
    <div class="band band--top"></div>

    <div class="brand">
      <div class="brand__square"></div>
      <div class="brand__name">TRELVIX</div>
    </div>
    <div class="brand__web">www.trelvix-soft.com</div>

    <div class="details">
      <h1 class="details__name">Mr. Someone</h1>
      <p class="details__role">Director</p>
      <address class="details__address">address somewhere<br>Brazil</address>
      <ul class="details__contact">
        <li><span class="details__label">tel:</span>1-555-787-9090</li>
        <li>cell: 1-555-000-9090</li>
        <li>information@trelvix-soft.com</li>
      </ul>
    </div>

    <div class="band band--bottom"></div>
  </section>
</main>
</body>
</html>
```